Need a business card design for a new business

The business is going to be called "The Maple Lectern" - it is an online training company that provides Instructor Lead training to students at any destination in the world
The reference to cloud is the internet and classroom reference will be a computer at the students and instructors end

We will need a Web site and stationary and advertising material developed over time but for now require the business cards only

So if we are happy with the business card then we will use the same designers for the other requirments of the business as it evolves

Industry/Entity Type

Advertising

```html
<!DOCTYPE html>
<html lang="en">
<head>
<meta charset="utf-8">
<title>The Maple Lectern – Business Cards</title>
<link rel="stylesheet" href="https://fonts.googleapis.com/css2?family=Ubuntu:ital,wght@0,400;0,500;0,700;1,700&display=swap">
<style>
  :root {
    --page-bg: #ffffff;
    --card-white: #ffffff;
    --card-dark: #38383a;
    --brand-navy: #003a5c;
    --text-dark: #333335;
    --text-grey: #3c3c3e;
    --divider: #ffffff;
    --card-shadow: rgba(0, 0, 0, 0.22);
  }
  * { margin: 0; padding: 0; box-sizing: border-box; }
  html, body {
    width: 1200px;
    height: 891px;
    overflow: hidden;
    background: var(--page-bg);
    font-family: "Ubuntu", sans-serif;
  }
  .canvas {
    position: relative;
    width: 1200px;
    height: 891px;
  }
  .card {
    position: absolute;
    top: 45px;
    width: 486px;
    height: 798px;
    border-radius: 30px;
    overflow: hidden;
    box-shadow: 0 8px 22px var(--card-shadow);
  }

  /* Front card */
  .card--front {
    left: 63px;
    background: var(--card-white);
  }
  .front-wordmark {
    position: absolute;
    left: 48px;
    top: 62px;
    font-weight: 500;
    font-size: 36px;
    line-height: 40px;
    color: var(--text-dark);
  }
  .accent-bar {
    position: absolute;
    left: 0;
    top: 570px;
    width: 45px;
    height: 183px;
    background: var(--card-dark);
  }
  .holder {
    position: absolute;
    left: 72px;
    top: 568px;
  }
  .holder-name {
    font-weight: 500;
    font-size: 42px;
    line-height: 48px;
    color: var(--brand-navy);
  }
  .holder-role {
    font-weight: 700;
    font-style: italic;
    font-size: 28px;
    line-height: 32px;
    color: var(--text-grey);
  }
  .contact {
    position: absolute;
    left: 72px;
    top: 682px;
    list-style: none;
    font-size: 18.5px;
    line-height: 26px;
    font-weight: 500;
    color: var(--text-dark);
  }
  .contact-label {
    font-weight: 700;
    color: var(--brand-navy);
  }

  /* Back card */
  .card--back {
    left: 657px;
    background: var(--card-dark);
  }
  .back-wordmark {
    position: absolute;
    left: 0;
    right: 0;
    top: 270px;
    text-align: center;
    font-weight: 500;
    font-size: 62px;
    line-height: 70px;
    color: var(--card-white);
  }
  .back-divider {
    position: absolute;
    left: 0;
    right: 0;
    top: 679px;
    height: 6px;
    background: var(--divider);
  }
  .web-band {
    position: absolute;
    left: 0;
    right: 0;
    top: 687px;
    bottom: 0;
    background: var(--brand-navy);
    display: flex;
    align-items: center;
    justify-content: center;
  }
  .web-address {
    font-weight: 500;
    font-size: 30px;
    color: var(--card-white);
    padding-top: 2px;
  }
</style>
</head>
<body>
<main class="canvas">
  <section class="card card--front" aria-label="Business card front">
    <div class="front-wordmark">The Maple<br>Lectern</div>
    <div class="accent-bar"></div>
    <div class="holder">
      <p class="holder-name">Martin Hale</p>
      <p class="holder-role">Manager</p>
    </div>
    <ul class="contact">
      <li><span class="contact-label">phone:</span> 01482-60317</li>
      <li><span class="contact-label">e-mail:</span> m.hale@maplelectern.com</li>
      <li><span class="contact-label">address:</span> 14 Birch Avenue, City Code</li>
    </ul>
  </section>

  <section class="card card--back" aria-label="Business card back">
    <div class="back-wordmark">The Maple<br>Lectern</div>
    <div class="back-divider"></div>
    <div class="web-band">
      <p class="web-address">www.TheMapleLectern.com</p>
    </div>
  </section>
</main>
</body>
</html>
```